I need a business card design for a new company that will be doing consulting work around issues of cultural competency, and diversity and inclusion. I would like the design to be crisp and clear with bold but conservative colors and incorporate shades of blue

Target Market(s)

Small businesses, schools, non-profits

Industry/Entity Type

Consulting

Font styles to use
Serif
Sans Serif

Colors
0c5ba6
6b449b
3276b5
0292cd

Requirements
Must have
• A Morrow Venture (name of company)
• Lemlem Tavish
• CEO
• lemlem@amorrowventure.com
• (215)483-2756

```html
<!DOCTYPE html>
<html lang="en">
<head>
<meta charset="utf-8">
<title>A Morrow Venture — Business Card</title>
<link href="https://fonts.googleapis.com/css2?family=Montserrat:wght@600;700&family=PT+Sans:wght@400&display=swap" rel="stylesheet">
<style>
  :root {
    --page-bg: #ececee;
    --card-purple: #6b449b;
    --card-purple-light: #7d52b8;
    --card-purple-deep: #5e3b8f;
    --band-blue: #0292cd;
    --rule-blue: #3276b5;
    --ink-white: #ffffff;
  }
  * { margin: 0; padding: 0; box-sizing: border-box; }
  html, body {
    width: 1200px; height: 1200px; overflow: hidden;
    background: var(--page-bg);
  }
  .canvas {
    position: relative; width: 1200px; height: 1200px;
    display: flex; align-items: center; justify-content: center;
  }
  .card {
    position: relative; width: 1050px; height: 600px; overflow: hidden;
    box-shadow: 0 18px 40px rgba(0,0,0,0.18);
  }
  .card-texture {
    position: absolute; inset: 0;
    background:
      radial-gradient(ellipse at 75% 70%, var(--card-purple-light) 0%, transparent 55%),
      radial-gradient(ellipse at 20% 30%, var(--card-purple-light) 0%, transparent 50%),
      linear-gradient(160deg, var(--card-purple) 0%, var(--card-purple-deep) 100%);
  }
  .name-band {
    position: absolute; left: 0; right: 0; top: 108px; height: 104px;
    background: var(--band-blue);
    display: flex; align-items: center; justify-content: center;
  }
  .name-band::before, .name-band::after {
    content: ""; position: absolute; left: 0; right: 0; height: 2px;
    background: var(--rule-blue); opacity: 0.7;
  }
  .name-band::before { top: 7px; }
  .name-band::after { bottom: 7px; }
  .company-name {
    font-family: "Montserrat", sans-serif; font-weight: 700;
    font-size: 60px; letter-spacing: 1px; text-transform: uppercase;
    color: var(--ink-white);
  }
  .person-frame {
    position: absolute; left: 50%; top: 268px; transform: translateX(-50%);
    width: 470px; height: 150px;
    border: 4px solid var(--ink-white); border-bottom: none;
    display: flex; flex-direction: column; justify-content: space-between;
  }
  .person-name {
    font-family: "Montserrat", sans-serif; font-weight: 600;
    font-size: 64px; color: var(--ink-white); text-align: center;
    margin-top: 20px; line-height: 1;
  }
  .person-role-row {
    display: flex; align-items: center; gap: 14px;
    margin: 0 -4px -16px;
  }
  .person-role-row .rule { flex: 1; height: 4px; background: var(--ink-white); }
  .person-role {
    font-family: "PT Sans", sans-serif; font-size: 28px;
    color: var(--ink-white); line-height: 1;
  }
  .contact-line {
    position: absolute; left: 0; right: 0; bottom: 78px;
    display: flex; justify-content: center; gap: 44px;
    font-family: "PT Sans", sans-serif; font-size: 34px; color: var(--ink-white);
  }
  .contact-item { display: flex; align-items: center; gap: 12px; }
  .contact-icon { width: 26px; height: 26px; fill: var(--ink-white); }
</style>
</head>
<body>
<main class="canvas">
  <section class="card">
    <div class="card-texture" role="img" aria-label="Soft purple water-ripple texture background"></div>

    <div class="name-band">
      <h1 class="company-name">A Morrow Venture</h1>
    </div>

    <div class="person-frame">
      <h2 class="person-name">Lemlem Tavish</h2>
      <div class="person-role-row">
        <span class="rule"></span>
        <span class="person-role">CEO</span>
        <span class="rule"></span>
      </div>
    </div>

    <div class="contact-line">
      <span class="contact-item">
        <svg class="contact-icon" viewBox="0 0 24 24" aria-hidden="true">
          <path d="M6.6 10.8a15.1 15.1 0 0 0 6.6 6.6l2.2-2.2c.3-.3.7-.4 1-.2 1.1.4 2.3.6 3.6.6.6 0 1 .4 1 1V20c0 .6-.4 1-1 1A17 17 0 0 1 3 4c0-.6.4-1 1-1h3.5c.6 0 1 .4 1 1 0 1.3.2 2.5.6 3.6.1.3 0 .7-.2 1z"/>
        </svg>
        (215)483-2756
      </span>
      <span class="contact-item">
        <svg class="contact-icon" viewBox="0 0 24 24" aria-hidden="true">
          <path d="M2 5h20v14H2z" fill="none" stroke="#fff" stroke-width="2"/>
          <path d="M2 5l10 8 10-8" fill="none" stroke="#fff" stroke-width="2"/>
        </svg>
        lemlem@amorrowventure.com
      </span>
    </div>
  </section>
</main>
</body>
</html>
```